Business Card Design

we are a Business Training & Consulting company that specializes in Lean Six Sigma coaching & consulting. Our clients are Big Businesses and Consultancy firms. Need a card design that is minimalist and elegant.. need to feature logo of our KRV brand & probably at the back we also need to include the logo of the parent company (DORAMBE Business Group Pty. Ltd.)
Font needs to be consistent with our website font especially the KRV font on the website header.. (www.krvqa.example)
Hi All,
Industry/Entity Type
Business
Contact Information for Business Card
Marcus T Ellingrove
Director
Business Consultancy & Training Programs
www.krvqa.example
P.O. Box 5172,
Perth, Western Australia, 6164, Australia.
M: +61 4 5538 9071
T: 1 300 579 218
F: +61 8 9727 3185
marcus@krvqa.example
ABN # : 73 2951 807 36
ACN #: 295 180 736

```html
<!DOCTYPE html>
<html lang="en">
<head>
<meta charset="utf-8">
<title>KRV Training and Consultancy – Business Card</title>
<link rel="stylesheet" href="https://fonts.googleapis.com/css2?family=Questrial&family=Mulish:wght@700&display=swap">
<style>
  :root {
    --bg: #ecebe8;
    --card-white: #ffffff;
    --ink: #3d3d3f;
    --ink-soft: #5b5b60;
    --rule: #b9b9bd;
    --blue-deep: #0a3580;
    --blue-mid: #0d4f9e;
    --blue-light: #2a6fc0;
    --on-blue: #e8f0fb;
    --accent-blue: #5fb4ea;
    --logo-blue: #1f5fae;
  }
  * { margin: 0; padding: 0; box-sizing: border-box; }
  html, body { width: 1200px; height: 800px; overflow: hidden; }
  body {
    background: var(--bg);
    font-family: "Questrial", "Century Gothic", sans-serif;
    position: relative;
  }
  .card {
    position: absolute;
    top: 235px;
    width: 540px;
    height: 330px;
    border-radius: 4px;
    box-shadow: 0 10px 28px rgba(0,0,0,.16), 0 2px 6px rgba(0,0,0,.1);
    overflow: hidden;
  }

  /* Back of card */
  .card-back {
    left: 40px;
    background: linear-gradient(160deg, var(--blue-light) 0%, var(--blue-mid) 40%, var(--blue-deep) 100%);
    color: var(--on-blue);
  }
  .registration {
    position: absolute;
    left: 22px;
    top: 165px;
    transform: translate(-50%, -50%) rotate(-90deg);
    transform-origin: center;
    white-space: nowrap;
    font-size: 11px;
    letter-spacing: .5px;
    margin-left: 0;
    opacity: .85;
  }
  .web-address {
    position: absolute;
    left: 0; right: 0;
    top: 128px;
    text-align: center;
    font-size: 26px;
    letter-spacing: .3px;
    color: #fff;
  }
  .parent-line {
    position: absolute;
    right: 150px;
    top: 222px;
    text-align: right;
    font-size: 15px;
    line-height: 1.25;
  }
  .parent-mark {
    position: absolute;
    right: 26px;
    top: 232px;
    display: flex;
    align-items: center;
    gap: 7px;
  }
  .parent-mark .dot {
    width: 12px; height: 12px; border-radius: 50%;
    background: var(--accent-blue);
  }
  .parent-mark .name {
    font-size: 18px;
    color: var(--accent-blue);
    letter-spacing: 1px;
  }

  /* Front of card */
  .card-front {
    left: 620px;
    background: var(--card-white);
    color: var(--ink);
  }
  .brand-mark {
    position: absolute;
    left: 34px;
    top: 34px;
    display: flex;
    align-items: center;
    gap: 10px;
  }
  .brand-mark .dot {
    width: 46px; height: 46px; border-radius: 50%;
    background: var(--logo-blue);
  }
  .brand-mark .name {
    font-size: 28px;
    color: var(--logo-blue);
    letter-spacing: 2px;
  }
  .company {
    position: absolute;
    right: 30px;
    top: 104px;
    text-align: right;
  }
  .company-name {
    font-size: 25px;
    color: var(--ink);
    letter-spacing: .2px;
  }
  .company-tagline {
    font-size: 13px;
    line-height: 1.3;
    color: var(--ink-soft);
    margin-top: 2px;
  }
  .person {
    position: absolute;
    right: 300px;
    top: 190px;
    text-align: right;
    font-size: 12px;
    line-height: 1.35;
    color: var(--ink-soft);
  }
  .person-name {
    font-family: "Mulish", "Century Gothic", sans-serif;
    font-weight: 700;
    font-size: 15px;
    color: var(--ink);
    margin-bottom: 2px;
  }
  .divider {
    position: absolute;
    left: 254px;
    top: 190px;
    width: 1px;
    height: 100px;
    background: var(--rule);
  }
  .contact {
    position: absolute;
    left: 268px;
    top: 222px;
    font-size: 12px;
    line-height: 1.45;
    color: var(--ink-soft);
    list-style: none;
  }
</style>
</head>
<body>

  <section class="card card-back" aria-label="Back of business card">
    <p class="registration">ABN # 73 2951 807 36 ACN # 295 180 736</p>
    <p class="web-address">www.krvqa.example</p>
    <p class="parent-line">A part of the<br>DORAMBE<br>Business Group Pty. Ltd.</p>
    <div class="parent-mark">
      <span class="dot"></span>
      <span class="name">DORAMBE</span>
    </div>
  </section>

  <section class="card card-front" aria-label="Front of business card">
    <div class="brand-mark">
      <span class="dot"></span>
      <span class="name">KRV</span>
    </div>
    <div class="company">
      <p class="company-name">KRV Training and Consultancy</p>
      <p class="company-tagline">Performance Improvement Methodologies<br>Training &amp; Consultancy</p>
    </div>
    <div class="person">
      <p class="person-name">Marcus T Ellingrove</p>
      <p>Director Business<br>Consultancy &amp; Training Programs</p>
    </div>
    <span class="divider"></span>
    <ul class="contact">
      <li>P.O. Box 5172, Perth, Western Australia, 6164</li>
      <li>M: +61 4 5538 9071</li>
      <li>T: 1 300 579 218</li>
      <li>F: +61 8 9727 3185</li>
      <li>marcus@krvqa.example</li>
    </ul>
  </section>

</body>
</html>
```